TK Fiscal Website Redesign Contest

We want to refresh our website to be more insitutional, professional for an international audience. We have designed a new logo for this purpose and that has been attached. A full brand brief and positioning statement has also been attached. Please read through all the documents carefully before designing. The old website is found here: https://tk-fiscal-example.com/

Target Market(s)

Actuaries and associated businesses internationally

Industry/Entity Type

professional services - actuaries

Number of Pages Required

3 page

Font styles to use
Sans Serif

Colors
0054AA
0677BA
7BADD7
CADEEF
E8F1F8
0094D4
00A9DD
6FCCEA
C7EBF8
E9F6FB
F0912C
F2A743
F7CA91
FBE8D2
FDF5EE
EE7325
F08F49
F5BC92
FAE3D3
FDF4ED
EB3D1F
EC4F4E
F09395
F8D3D4
FCEDEE

Requirements
Must have
• blues and greens to match the logo color, complimentary colors, navigation
Nice to have
• old site: https://tk-fiscal-example.com/

```html
<!DOCTYPE html>
<html lang="en">
<head>
<meta charset="utf-8">
<title>TK Fiscal — Actuarial software</title>
<link href="https://fonts.googleapis.com/css2?family=Inter:wght@400;500;600;700&display=swap" rel="stylesheet">
<style>
:root{
  --ink:#1d1f24;
  --body:#3a3d44;
  --blue-deep:#0054AA;
  --blue-mid:#0677BA;
  --blue-bright:#0094D4;
  --cyan:#00A9DD;
  --cyan-soft:#6FCCEA;
  --pale:#F2F5FD;
  --line:#C9D6F5;
  --orange:#FF7A12;
  --white:#ffffff;
}
*{box-sizing:border-box;margin:0;padding:0}
html,body{width:1200px;height:3337px;overflow:hidden}
body{position:relative;font-family:"Inter",Arial,sans-serif;color:var(--ink);background:var(--white)}
.abs{position:absolute}
.center{left:0;width:1200px;text-align:center}
.btn{position:absolute;background:var(--orange);color:var(--white);font-weight:700;font-size:14px;display:flex;align-items:center;justify-content:center;border-radius:3px;text-decoration:none}
.eyebrow{position:absolute;font-size:17px;font-weight:500;letter-spacing:.3px;background:linear-gradient(90deg,var(--blue-bright),var(--cyan));-webkit-background-clip:text;background-clip:text;color:transparent}
.h2{position:absolute;font-size:40px;font-weight:500;line-height:41px;letter-spacing:-.5px;color:var(--ink)}
.blob{position:absolute;border-radius:50%;filter:blur(40px)}

/* hero */
.hero{position:absolute;left:0;top:0;width:1200px;height:483px;overflow:hidden;background:linear-gradient(180deg,#fff 0%,#f6f8fe 100%)}
.nav-brand{position:absolute;left:111px;top:28px;font-size:25px;font-weight:500;letter-spacing:1.5px;color:var(--ink)}
.nav{position:absolute;top:33px;left:402px;display:flex;gap:19px;font-size:14px;color:var(--ink)}
.hero-title{position:absolute;top:123px;font-size:49px;font-weight:500;line-height:52px;letter-spacing:-.8px}
.grad-text{background:linear-gradient(90deg,#0a6cf5,var(--cyan));-webkit-background-clip:text;background-clip:text;color:transparent}
.hero-sub{position:absolute;top:293px;font-size:16px;line-height:26px;color:var(--body)}

/* platform */
.platform{position:absolute;left:0;top:483px;width:1200px;height:493px;background:var(--pale)}
.para{position:absolute;font-size:15.5px;line-height:26px;color:var(--body)}
.node-label{position:absolute;font-size:15px;color:var(--ink)}
.node-label b{font-weight:600}

/* cards */
.card{position:absolute;border:1.5px solid var(--line);background:#F4F7FE}
.card h3{position:absolute;left:28px;top:120px;font-size:19px;font-weight:600;color:var(--ink)}
.card p{position:absolute;left:28px;top:153px;width:260px;font-size:15px;line-height:26px;color:var(--body)}
.card .arrow{position:absolute;left:28px}

.feature{position:absolute;width:240px;text-align:center;font-size:15px;line-height:26px;color:var(--body)}

.insight{position:absolute;top:2351px;width:315px;height:196px;border:1.5px solid var(--line);background:#fff}
.insight .tag{position:absolute;left:27px;top:36px;font-size:15px;color:var(--body);display:flex;align-items:center;gap:11px}
.insight .tag i{width:8px;height:8px;border-radius:50%;background:linear-gradient(135deg,var(--cyan),#0a5cf5)}
.insight h3{position:absolute;left:27px;top:67px;width:275px;font-size:19px;font-weight:500;line-height:26px;color:var(--ink)}
.insight .arrow{position:absolute;left:27px;top:152px}

/* footer */
.footer{position:absolute;left:0;top:3075px;width:1200px;height:262px;background:linear-gradient(90deg,#1aa7e4 0%,#0f7ff0 55%,#0a52f5 100%);color:var(--white)}
.footer-brand{position:absolute;left:111px;top:80px;font-size:33px;font-weight:500;letter-spacing:2px}
.footer a{color:var(--white);text-decoration:none}
</style>
</head>
<body>

<section class="hero">
  <div class="blob" style="left:-90px;top:60px;width:260px;height:300px;background:#5d88ff;opacity:.75"></div>
  <div class="blob" style="left:980px;top:0;width:260px;height:300px;background:#5b8cff;opacity:.8"></div>
  <div class="blob" style="left:-60px;top:330px;width:500px;height:260px;background:#7ba3ff;opacity:.6"></div>
  <div class="blob" style="left:760px;top:300px;width:520px;height:280px;background:#93b4ff;opacity:.55"></div>

  <div class="nav-brand">TK Fiscal</div>
  <nav class="nav"><span>Home</span><span>Platform</span><span>Solutions</span><span>Insights</span><span>Company</span><span>Contact</span></nav>
  <a class="btn" style="left:845px;top:21px;width:244px;height:41px">Request a Technical Walkthrough</a>

  <h1 class="hero-title center">Actuarial software for<br>structured, auditable<br><span class="grad-text">financial analysis</span></h1>
  <p class="hero-sub center">Software that translates actuarial methodologies into disciplined<br>decision-ready analytical tools across diverse regulatory environments.</p>
  <a class="btn" style="left:469px;top:369px;width:262px;height:43px">Request a Technical Walkthrough</a>
</section>

<section class="platform">
  <div class="eyebrow" style="left:113px;top:106px">PLATFORM</div>
  <h2 class="h2" style="left:111px;top:137px">Modular software for<br>actuarial workflows</h2>
  <p class="para" style="left:111px;top:239px">TK Fiscal develops modular actuarial software designed<br>to support reserving, valuation, pricing, and risk analysis<br>workflows across diverse regulatory environments.</p>
  <a class="btn" style="left:111px;top:341px;width:184px;height:42px">Explore Platform</a>

  <svg class="abs" style="left:685px;top:41px" width="400" height="400" viewBox="0 0 400 400" aria-label="Workflow cycle: input, analysis, review, output">
    <defs>
      <linearGradient id="ig" x1="0" y1="0" x2="1" y2="1"><stop offset="0" stop-color="#2ad0f0"/><stop offset="1" stop-color="#0a55f5"/></linearGradient>
    </defs>
    <circle cx="200" cy="200" r="120" fill="none" stroke="#e3e9f8" stroke-width="2"/>
    <circle cx="200" cy="200" r="100" fill="#f7f9ff"/>
    <g fill="#fff" stroke="#d5def5" stroke-width="1.5">
      <circle cx="200" cy="80" r="38"/><circle cx="320" cy="200" r="38"/>
      <circle cx="200" cy="320" r="38"/><circle cx="80" cy="200" r="38"/>
    </g>
    <circle cx="200" cy="80" r="18" fill="url(#ig)"/>
    <path d="M191 80h16M200 72l8 8-8 8" stroke="#fff" stroke-width="3" fill="none" stroke-linecap="round"/>
    <g fill="url(#ig)"><rect x="306" y="200" width="6" height="14"/><rect x="316" y="193" width="6" height="21"/><rect x="326" y="187" width="6" height="27"/></g>
    <path d="M304 194l10-8 8 4 14-12" stroke="url(#ig)" stroke-width="3" fill="none"/>
    <rect x="186" y="306" width="28" height="22" rx="3" fill="url(#ig)"/>
    <path d="M191 313h12M191 319h14" stroke="#fff" stroke-width="2"/>
    <path d="M80 186v20M71 195l9-9 9 9M66 206v9h28v-9" stroke="url(#ig)" stroke-width="4" fill="none" stroke-linecap="round"/>
    <text x="200" y="206" text-anchor="middle" font-family="Inter,Arial,sans-serif" font-size="15" font-weight="500" letter-spacing="1" fill="#1d1f24">TK Fiscal</text>
  </svg>
  <div class="node-label" style="left:856px;top:58px">01 <b>Input</b></div>
  <div class="node-label" style="left:1047px;top:232px">02 <b>Analysis</b></div>
  <div class="node-label" style="left:846px;top:417px">03 <b>Review</b></div>
  <div class="node-label" style="left:638px;top:233px">04 <b>Output</b></div>
</section>

<div class="eyebrow center" style="top:1069px">SOLUTIONS</div>
<h2 class="h2 center" style="top:1102px">Three pillars of<br>actuarial software</h2>

<svg width="0" height="0" style="position:absolute"><defs>
  <linearGradient id="cg" x1="0" y1="0" x2="1" y2="1"><stop offset="0" stop-color="#2ad0f0"/><stop offset="1" stop-color="#0a4cf5"/></linearGradient>
  <symbol id="arrow" viewBox="0 0 44 14"><path d="M0 7h42M36 1l6 6-6 6" stroke="#1d4fe0" stroke-width="1.8" fill="none"/></symbol>
</defs></svg>

<div class="card" style="left:111px;top:1231px;width:315px;height:315px">
  <svg class="abs" style="left:28px;top:39px" width="52" height="52" viewBox="0 0 52 52"><path d="M26 2l4 8 9 1-6 6 2 9-9-5-8 5 2-9-6-6 9-1z" fill="url(#cg)"/><circle cx="8" cy="22" r="5" fill="#2ad0f0"/><circle cx="44" cy="22" r="5" fill="#0a6cf5"/><g fill="url(#cg)"><rect x="2" y="34" width="14" height="7"/><rect x="19" y="34" width="14" height="7"/><rect x="36" y="34" width="14" height="7"/><rect x="2" y="43" width="14" height="7"/><rect x="19" y="43" width="14" height="7"/><rect x="36" y="43" width="14" height="7"/></g></svg>
  <h3>Reserving &amp; Valuation</h3>
  <p>Software supporting structured reserving workflows and financial reporting across jurisdictions.</p>
  <svg class="arrow" style="top:262px" width="44" height="14"><use href="#arrow"/></svg>
</div>
<div class="card" style="left:443px;top:1231px;width:315px;height:315px">
  <svg class="abs" style="left:28px;top:39px" width="52" height="52" viewBox="0 0 52 52"><circle cx="26" cy="26" r="25" fill="url(#cg)"/><text x="26" y="35" text-anchor="middle" font-family="Inter,Arial,sans-serif" font-size="26" font-weight="700" fill="#fff">$</text></svg>
  <h3>Pricing</h3>
  <p>Models supporting insurance and reinsurance pricing based on actuarial methodologies.</p>
  <svg class="arrow" style="top:262px" width="44" height="14"><use href="#arrow"/></svg>
</div>
<div class="card" style="left:775px;top:1231px;width:315px;height:315px">
  <svg class="abs" style="left:28px;top:39px" width="52" height="52" viewBox="0 0 52 52"><circle cx="26" cy="22" r="17" fill="none" stroke="url(#cg)" stroke-width="7" stroke-dasharray="6 3"/><path d="M26 16l14 32H12z" fill="url(#cg)"/><path d="M26 28v10M26 42v2" stroke="#fff" stroke-width="3"/></svg>
  <h3>Enterprise Risk Management</h3>
  <p>Software supporting reinsurance optimization and capital modeling.</p>
  <svg class="arrow" style="top:262px" width="44" height="14"><use href="#arrow"/></svg>
</div>

<div class="eyebrow center" style="top:1671px">CHARACTERISTICS</div>
<h2 class="h2 center" style="top:1704px">Built for rigour, designed<br>for clarity</h2>

<svg class="abs" style="left:0;top:1826px" width="1200" height="120" viewBox="0 0 1200 120">
  <defs>
    <radialGradient id="halo"><stop offset=".7" stop-color="#9fdcf5"/><stop offset="1" stop-color="#c7d8ff"/></radialGradient>
  </defs>
  <g>
    <circle cx="219" cy="60" r="57" fill="url(#halo)"/><circle cx="219" cy="60" r="44" fill="url(#cg)"/>
    <circle cx="473" cy="60" r="57" fill="url(#halo)"/><circle cx="473" cy="60" r="44" fill="url(#cg)"/>
    <circle cx="726" cy="60" r="57" fill="url(#halo)"/><circle cx="726" cy="60" r="44" fill="url(#cg)"/>
    <circle cx="980" cy="60" r="57" fill="url(#halo)"/><circle cx="980" cy="60" r="44" fill="url(#cg)"/>
  </g>
  <g fill="none" stroke="#fff" stroke-width="3" stroke-linecap="round">
    <rect x="199" y="44" width="20" height="10" rx="2"/><rect x="219" y="66" width="20" height="10" rx="2"/><path d="M204 54v17h15M224 49h10v17"/>
    <circle cx="469" cy="62" r="16"/><circle cx="479" cy="56" r="12" fill="#fff" fill-opacity=".35"/>
    <circle cx="721" cy="56" r="16"/><path d="M733 68l12 12M714 62v-4M721 62v-10M728 62v-7"/>
    <rect x="964" y="40" width="26" height="22" rx="3"/><path d="M970 48h14M970 54h10M978 62l4 14 8-8h6"/>
  </g>
</svg>
<div class="feature" style="left:99px;top:1957px">Structured workflows suitable<br>for multi-jurisdictional review</div>
<div class="feature" style="left:353px;top:1957px">Transparent assumptions and<br>methodological clarity</div>
<div class="feature" style="left:606px;top:1957px">Comparative scenario analysis</div>
<div class="feature" style="left:860px;top:1957px">Supports professional<br>judgment rather than replacing it</div>

<section class="abs" style="left:0;top:2115px;width:1200px;height:960px;overflow:hidden;background:#f3f6fd">
  <div class="blob" style="left:-80px;top:380px;width:520px;height:300px;background:#5d8bff;opacity:.65"></div>
  <div class="blob" style="left:-100px;top:780px;width:260px;height:260px;background:#6d98ff;opacity:.55"></div>
  <div class="blob" style="left:960px;top:720px;width:320px;height:300px;background:#5b8cff;opacity:.7"></div>
  <div class="abs" style="left:0;top:430px;width:1200px;height:530px;background:linear-gradient(180deg,rgba(255,255,255,0) 0%,rgba(255,255,255,.75) 35%,rgba(255,255,255,.6) 100%)"></div>
</section>

<div class="eyebrow center" style="top:2190px">INSIGHTS</div>
<h2 class="h2 center" style="top:2222px">Practitioner-level<br>perspectives</h2>

<div class="insight" style="left:111px">
  <div class="tag"><i></i>Methodology</div>
  <h3>Methodological perspectives in actuarial reserving</h3>
  <svg class="arrow" width="44" height="14"><use href="#arrow"/></svg>
</div>
<div class="insight" style="left:443px">
  <div class="tag"><i></i>Governance</div>
  <h3>Governance considerations in multi-jurisdictional analysis</h3>
  <svg class="arrow" width="44" height="14"><use href="#arrow"/></svg>
</div>
<div class="insight" style="left:775px">
  <div class="tag"><i></i>Practice</div>
  <h3>Observations on actuarial practice in emerging markets</h3>
  <svg class="arrow" width="44" height="14"><use href="#arrow"/></svg>
</div>
<a class="btn" style="left:508px;top:2579px;width:184px;height:42px">Read Insights</a>

<h2 class="h2 center" style="top:2773px">Interested in exploring<br>the platform?</h2>
<p class="para center" style="top:2874px">Schedule a technical walkthrough with our team to understand<br>how TK Fiscal can support your actuarial workflows.</p>
<a class="btn" style="left:469px;top:2955px;width:262px;height:42px">Request a Technical Walkthrough</a>

<footer class="footer">
  <div class="footer-brand">TK Fiscal</div>
  <div class="abs" style="left:114px;top:140px;font-size:17px;font-weight:600;display:flex;align-items:center;gap:8px">Connect with us: <span style="display:inline-block;width:28px;height:28px;border-radius:50%;background:#fff;opacity:.9"></span></div>
  <div class="abs" style="left:114px;top:193px;font-size:15px">2026 TK Fiscal. All Rights Reserved.</div>

  <div class="abs" style="left:741px;top:86px;font-size:17px;font-weight:600">Quick Links</div>
  <div class="abs" style="left:741px;top:117px;font-size:14px;line-height:26px"><a>Company</a><br><a>Platform</a><br><a>Solutions</a><br><a>Insights</a></div>

  <div class="abs" style="left:921px;top:86px;font-size:17px;font-weight:600;line-height:26px">TK Fiscal,<br>Address, comes here</div>
  <div class="abs" style="left:921px;top:152px;font-size:15px;line-height:25px"><b>P:</b> +1 555-010-2040<br><b>E:</b> info@tkfiscal-example.com</div>
</footer>

</body>
</html>
```